R T Security Flyer - Security Based Company

Security company offering installation of CCTV and Intruder alarm systems mainly but not limited to home alarms. Feel free to be creative

Target Market(s)

Residential and Commercial properties, Facility Managers, local business

Requirements
Must have
• smart professional finish, logo and latest up to date pictures if on kit

```html
<!DOCTYPE html>
<html lang="en">
<head>
<meta charset="utf-8">
<title>R T Security Flyer</title>
<link href="https://fonts.googleapis.com/css2?family=Montserrat:wght@600;700;800;900&family=Hind:wght@400;500;600&display=swap" rel="stylesheet">
<style>
:root{
  --backdrop:#2b2b2d;
  --navy:#1b2036;
  --orange:#e8401c;
  --orange-bright:#f15a24;
  --white:#ffffff;
  --ink:#1d1d24;
  --grey:#e6e7ea;
}
*{box-sizing:border-box;margin:0;padding:0}
html,body{width:1200px;height:858px;overflow:hidden;background:var(--backdrop)}
body{position:relative;font-family:"Hind",Arial,sans-serif;color:var(--ink)}
.page{position:absolute;top:63px;width:518px;height:732px;background:var(--white);overflow:hidden}
.page--front{left:64px}
.page--back{left:618px}
.abs{position:absolute}
.bg{position:absolute;left:0;top:0}
.headline{left:30px;top:36px;width:258px;color:var(--orange-bright);font-family:"Montserrat",sans-serif;font-weight:900;text-transform:uppercase;line-height:1;white-space:nowrap}
.headline .small{display:block;font-size:19.5px;line-height:26px;letter-spacing:-.2px}
.headline .mid{display:block;font-size:40px;line-height:46px;letter-spacing:-.8px}
.headline .big{display:block;font-size:64px;line-height:66px;letter-spacing:-1.5px}
.placeholder{position:absolute}
.phones{background:linear-gradient(135deg,#2f3a5a,#5a93d0 45%,#e9ecf0 60%,#c7ccd3)}
.house{background:radial-gradient(ellipse at 40% 60%,#8fc46a 0%,#cdd6dc 45%,#f2f3f5 75%);border-radius:40px 10px 40px 10px}
.logo-ring{border-radius:50%;background:var(--white);border:7px solid var(--orange);display:flex;flex-direction:column;align-items:center;justify-content:center;text-align:center}
.logo-square{width:40px;height:40px;background:var(--orange);margin-bottom:10px}
.logo-name{font-family:"Montserrat",sans-serif;font-weight:800;color:var(--orange);font-size:17px;letter-spacing:.3px}
.logo-sub{font-family:"Montserrat",sans-serif;font-weight:600;color:var(--orange);font-size:11px;letter-spacing:3px;margin-top:2px}
.features{left:24px;top:459px;width:262px;list-style:none}
.features li{position:relative;padding-left:20px;font-size:8.2px;line-height:10px;margin-bottom:6.4px;color:var(--ink);font-weight:500}
.features svg{position:absolute;left:0;top:0}
.quote{left:294px;top:441px;width:206px;height:198px}
.quote-text{position:absolute;left:0;top:9px;width:206px;text-align:center;color:var(--white);font-size:9.6px;line-height:12px}
.quote-text .lead{font-size:9px;margin-top:6px;display:block}
.quote-text .free{display:block;font-family:"Montserrat",sans-serif;font-weight:800;font-size:20px;line-height:24px}
.kitchen{left:10px;top:104px;width:186px;height:88px;background:linear-gradient(90deg,#dfe4ea,#b9c3cc 50%,#8c7a66)}
.footer{left:0;top:638px;width:518px;height:94px}
.footer-left{position:absolute;left:0;top:0;width:294px;height:94px;background:var(--grey)}
.footer-right{position:absolute;left:294px;top:0;width:224px;height:94px;background:var(--orange);color:var(--white);text-align:center;padding-top:22px}
.call{font-family:"Montserrat",sans-serif;font-weight:800;font-size:18px;line-height:22px;white-space:nowrap}
.contact{font-size:11px;line-height:14.5px;margin-top:2px}
.badge{position:absolute;top:17px;width:44px;text-align:center}
.badge .disc{width:42px;height:42px;border-radius:50%;border:3px solid #2a3d7a;background:var(--white);margin:0 auto}
.badge span{display:block;font-size:7px;line-height:8px;color:#23336a;font-weight:600;margin-top:2px}
.review{position:absolute;left:133px;top:20px}
.review-name{font-weight:600;font-size:16px;color:#2b5aa8;line-height:16px}
.review-tag{font-size:7px;color:var(--ink);margin-left:40px}
.partner{position:absolute;left:136px;top:52px;display:flex;align-items:center;gap:5px}
.partner i{width:12px;height:12px;border-radius:50%;background:#2b5aa8;display:block}
.partner b{font-weight:600;font-size:13px;color:#2b5aa8}
.intro{left:22px;top:38px;width:196px;font-family:"Montserrat",sans-serif;font-weight:700;font-size:14px;line-height:20.5px;color:var(--navy);white-space:nowrap}
.clock{left:56px;top:144px;font-family:"Montserrat",sans-serif;font-weight:900;font-size:50px;line-height:54px;color:var(--orange-bright);letter-spacing:-1px}
.devices{background:linear-gradient(90deg,#f4f5f7,#dfe2e6 40%,#f6f6f7 70%,#e4e6e9)}
.benefits-title{left:28px;top:286px;font-family:"Montserrat",sans-serif;font-weight:700;font-size:14.5px;line-height:23px;color:var(--orange-bright);white-space:nowrap}
.benefits{left:28px;top:365px;list-style:none;color:var(--white);font-size:10px;line-height:12.6px;font-weight:500}
.benefits li::before{content:"\25CF";font-size:7px;margin-right:4px;vertical-align:1px}
.promise{font-family:"Montserrat",sans-serif}
.promise .brand{display:flex;align-items:center;gap:4px;color:var(--orange);font-weight:700;font-size:8px;margin-bottom:8px}
.promise .brand i{width:16px;height:16px;background:var(--orange);display:block}
.promise .line1{font-weight:800;font-size:10.5px;line-height:12px;color:var(--ink)}
.promise .line2{font-weight:800;font-size:14.5px;line-height:16px;color:var(--orange);margin-top:6px}
.shot{position:absolute;top:461px;width:150px;height:100px;border:3px solid var(--orange)}
.shot1{left:28px;background:linear-gradient(135deg,#f1f2f4,#c9ced6)}
.shot2{left:184px;background:linear-gradient(135deg,#efe6dc,#b8a58f)}
.shot3{left:340px;background:linear-gradient(135deg,#e8eaee,#8e96a3)}
.summary{left:30px;top:577px;width:458px;text-align:center;color:var(--white);font-size:9px;line-height:11.5px}
</style>
</head>
<body>

<section class="page page--front">
  <svg class="bg" width="518" height="732" viewBox="0 0 518 732">
    <path d="M0 0H518V218C420 232 300 262 160 252 90 247 40 250 0 262Z" fill="var(--navy)"/>
    <path d="M0 262C40 250 90 247 160 252 300 262 420 232 518 218V238C420 250 300 282 160 276 90 272 40 276 0 288Z" fill="var(--orange)"/>
  </svg>

  <h1 class="abs headline">
    <span class="small">Are you looking</span>
    <span class="small">to keep you or your</span>
    <span class="mid">Premises</span>
    <span class="big">Safe?</span>
  </h1>

  <div class="placeholder phones" style="left:298px;top:26px;width:196px;height:198px;border-radius:14px" role="img" aria-label="Two smartphones showing a security control app"></div>

  <div class="abs logo-ring" style="left:34px;top:235px;width:168px;height:168px">
    <div class="logo-square"></div>
    <div class="logo-name">R T SECURITY</div>
    <div class="logo-sub">SYSTEMS</div>
  </div>

  <div class="placeholder house" style="left:210px;top:244px;width:300px;height:188px" role="img" aria-label="Cutaway illustration of a house fitted with alarm sensors and cameras"></div>

  <ul class="abs features">
    <li><svg width="12" height="12" viewBox="0 0 12 12"><circle cx="6" cy="6" r="5" fill="none" stroke="#1d1d24" stroke-width="1.2"/><path d="M3.5 6l2 2 4-5" fill="none" stroke="var(--orange)" stroke-width="1.6"/></svg>We install, maintain and repair all intruder alarms, CCTV, intercom and access control</li>
    <li><svg width="12" height="12" viewBox="0 0 12 12"><circle cx="6" cy="6" r="5" fill="none" stroke="#1d1d24" stroke-width="1.2"/><path d="M3.5 6l2 2 4-5" fill="none" stroke="var(--orange)" stroke-width="1.6"/></svg>View, control and manage your security systems anywhere in the world with smartphone apps</li>
    <li><svg width="12" height="12" viewBox="0 0 12 12"><circle cx="6" cy="6" r="5" fill="none" stroke="#1d1d24" stroke-width="1.2"/><path d="M3.5 6l2 2 4-5" fill="none" stroke="var(--orange)" stroke-width="1.6"/></svg>Feel at ease with monitoring services and police response tailored to suit you and your business</li>
    <li><svg width="12" height="12" viewBox="0 0 12 12"><circle cx="6" cy="6" r="5" fill="none" stroke="#1d1d24" stroke-width="1.2"/><path d="M3.5 6l2 2 4-5" fill="none" stroke="var(--orange)" stroke-width="1.6"/></svg>We can takeover any existing security system and offer maintenance checks to guarantee the best performance for you and your premises</li>
    <li><svg width="12" height="12" viewBox="0 0 12 12"><circle cx="6" cy="6" r="5" fill="none" stroke="#1d1d24" stroke-width="1.2"/><path d="M3.5 6l2 2 4-5" fill="none" stroke="var(--orange)" stroke-width="1.6"/></svg>We understand that being security conscious is ever increasing, protecting your property and family is a number one priority</li>
    <li><svg width="12" height="12" viewBox="0 0 12 12"><circle cx="6" cy="6" r="5" fill="none" stroke="#1d1d24" stroke-width="1.2"/><path d="M3.5 6l2 2 4-5" fill="none" stroke="var(--orange)" stroke-width="1.6"/></svg>Our fully insured and accredited team offer quality, safety and cost efficiency throughout and whole process</li>
  </ul>

  <div class="abs quote">
    <svg class="bg" width="206" height="198" viewBox="0 0 206 198">
      <path d="M0 14L103 0 206 14V198H0Z" fill="var(--orange)"/>
      <path d="M5 17L103 4 201 17V198H5Z" fill="none" stroke="#fff" stroke-width="1" opacity=".8"/>
    </svg>
    <p class="quote-text">If you are<br>looking to improve the<br>security in your home, office or<br>commercial property then
      <span class="lead">call a member of our team today for a</span>
      <span class="free">FREE QUOTE.</span>
    </p>
    <div class="placeholder kitchen" role="img" aria-label="Photo of a wall-mounted alarm panel in a modern kitchen"></div>
  </div>

  <footer class="abs footer">
    <div class="footer-left">
      <div class="badge" style="left:22px"><div class="disc"></div><span>Intruder Alarm Systems</span></div>
      <div class="badge" style="left:76px"><div class="disc"></div><span>CCTV Systems</span></div>
      <div class="review"><div class="review-name">TradeVouch</div><div class="review-tag">Trusted local reviews</div></div>
      <div class="partner"><i></i><b>Vantor Connect</b></div>
    </div>
    <div class="footer-right">
      <div class="call">Call: 01632 960418</div>
      <div class="contact">operations@rtsecuritysystems.co.uk<br>www.rtsecuritysystems.co.uk</div>
    </div>
  </footer>
</section>

<section class="page page--back">
  <svg class="bg" width="518" height="732" viewBox="0 0 518 732">
    <path d="M0 214C120 214 300 244 518 226V638H0Z" fill="var(--orange)"/>
    <path d="M0 232C120 228 300 262 518 246V638H0Z" fill="var(--navy)"/>
  </svg>

  <h2 class="abs intro">R T Security Systems Are<br>Using The Latest Cloud<br>-based Technology To<br>Stay Connected With<br>Your Home And Business</h2>
  <div class="abs clock">24/7</div>

  <div class="placeholder devices" style="left:222px;top:20px;width:296px;height:196px" role="img" aria-label="Cloud alarm hub, indoor camera, smart plug and wall sensors"></div>

  <h3 class="abs benefits-title">Some<br>Benefits Of<br>Cloud Services Are:</h3>

  <div class="placeholder phones" style="left:204px;top:226px;width:120px;height:132px;border-radius:10px" role="img" aria-label="Two smartphones showing the security control app"></div>

  <div class="abs logo-ring promise" style="left:322px;top:235px;width:168px;height:168px">
    <div class="brand"><i></i>R T SECURITY</div>
    <div class="line1">ARE ALWAYS THERE<br>ALWAYS AVAILABLE</div>
    <div class="line2">WHEREVER AND<br>WHENEVER YOU<br>NEED US.</div>
  </div>

  <ul class="abs benefits">
    <li>High level support 24/7</li>
    <li>Reduce engineer call outs and running costs</li>
    <li>Identify issues in advance</li>
    <li>Remotely manage systems to ensure correct operation</li>
    <li>Remote health checks carried out to keep your system performing as it should</li>
    <li>Automatically update your system with the latest releases via cloud application software</li>
    <li>Interact, control and integrate your security system like never before</li>
  </ul>

  <div class="shot shot1" role="img" aria-label="Hand pressing an alarm keypad"></div>
  <div class="shot shot2" role="img" aria-label="Person using the security app on a phone at a cafe table"></div>
  <div class="shot shot3" role="img" aria-label="Alarm keypad mounted in a bright hallway"></div>

  <p class="abs summary">With the new cloud-based system we can check the alarm performance anytime you need it. This gives us the capability to assist you in any of your needs, be that changing user codes or system configuration. We are always there, working in the background to make sure you have the support and help you need. This is taking alarm systems into the future and leaving the stand-alone systems in the past.</p>

  <footer class="abs footer">
    <div class="footer-left" style="width:286px">
      <div class="badge" style="left:28px"><div class="disc"></div><span>Intruder Alarm Systems</span></div>
      <div class="badge" style="left:82px"><div class="disc"></div><span>CCTV Systems</span></div>
      <div class="review" style="left:134px"><div class="review-name">TradeVouch</div><div class="review-tag">Trusted local reviews</div></div>
      <div class="partner" style="left:138px"><i></i><b>Vantor Connect</b></div>
    </div>
    <svg class="bg" style="left:270px" width="30" height="94" viewBox="0 0 30 94"><path d="M16 0H30V94H0Z" fill="var(--orange)"/></svg>
    <div class="footer-right" style="left:296px;width:222px">
      <div class="call">Call: 01632 960418</div>
      <div class="contact">operations@rtsecuritysystems.co.uk<br>www.rtsecuritysystems.co.uk</div>
    </div>
  </footer>
</section>

</body>
</html>
```